Premium Website Design for Wellness Practice Consulting Brand

I need a professional website design for my business, The Lanternfield Group.

Please see attached document for homepage formula instructions.

PLEASE NOTE THAT WE ARE NOT A CLINIC.

We are a consulting/strategy brand that helps established wellness practices grow by identifying what is holding them back in their marketing, website, positioning, and patient acquisition.

Our audience includes chiropractors, naturopaths, functional medicine clinics, acupuncturists, physical therapists, and other integrative or holistic practices.

The website needs to feel approachable premium.

It should feel polished, modern, trustworthy, and high-value, but not cold, stiff, or overly corporate.

At the same time, it must avoid looking like a clinic website.

We do not want stock medical visuals, treatment-room aesthetics, or anything that makes people think we provide patient care directly.

The brand should communicate:
- professional
- strategic
- trustworthy
- premium
- clear
- modern
- human
- relevant to wellness practice owners

The design should position us more like a consultant/strategist than a generic marketing agency.

Our main offer is not a long list of services.

Our core offer is helping practice owners see the “holes in the bucket” in their business and marketing, then giving them clarity on what needs to be fixed first.

So the design should support outcome-focused messaging, not “we do websites, SEO, ads, etc.”

Visual direction
I want inspiration from premium brands in the wellness business consulting space, especially the kind of direction seen on The Brightmoor Healer site: confident, elevated, human, and proof-driven, with images of people, leadership, clients, team interaction, wins, and transformation rather than clinical treatment imagery.

Their site emphasizes practitioner growth, leadership, systems, and measurable wins, which is closer to the feeling I want than a traditional clinic or agency site.

Important design goals
- Must clearly look like a business/consulting brand for wellness practices
- Must not be mistaken for a chiropractic, medical, or eye clinic website
- Must not feel tacky, cheap, or “internet marketer”
- Must not feel too sterile or disconnected from the wellness market
- Should feel credible enough for conferences, high-level partnerships, and premium service positioning
- Should feel welcoming enough that smaller or growing practices still feel comfortable reaching out

What I’m looking for
- Strong hierarchy and modern layout
- Clean typography
- Premium but warm color direction
- Smart use of whitespace
- A design that can support testimonials, case studies, authority, and clear calls to action
- A designer who understands brand positioning, not just decoration

Style notes
- Open to pairing DM Sans for body text with a more premium headline font
- Open to colors beyond the current brand mockups, as long as the final direction feels refined and high-trust
- Prefer real human/business-oriented imagery over clinic treatment imagery
- Minimal, elegant, strategic, and conversion-aware is better than flashy or over-designed

EXAMPLE WEBSITES:
This brand has similar target market as we do:
- https://thebrightmoorhealer.example

***The following Websites have a layout we like in terms of following a similar formula:
- https://harlowvalechiropractic.example
- https://brennochiropractic.example
- https://harlowvalemassagetherapy.example
- https://tollerbyphysiorehab.example
- https://orvidex.example

Target Market(s)

chiropractors, naturopaths, functional medicine clinics, acupuncturists, physical therapists, and other integrative or holistic practices.

Industry/Entity Type

Marketing / Consulting

Coding

Font styles to use
Sans Serif

Colors
0054AA
0677BA
7BADD7
CADEEF
E8F1F8

Requirements
Must have
• Home Page / About / Contact / Blog / Services / Testimonials

```html
<!DOCTYPE html>
<html lang="en">
<head>
<meta charset="utf-8">
<title>The Lanternfield Group – Homepage</title>
<link href="https://fonts.googleapis.com/css2?family=DM+Sans:wght@400;500;700&family=Poppins:wght@500;600;700&display=swap" rel="stylesheet">
<style>
:root{
  --blue-900:#0054AA;
  --blue-700:#0677BA;
  --blue-400:#7BADD7;
  --blue-200:#CADEEF;
  --blue-100:#E8F1F8;
  --ink:#1c2433;
  --muted:#5b6677;
  --dark:#101218;
  --navy:#0b2445;
  --white:#ffffff;
  --canvas:#eef2f6;
}
*{box-sizing:border-box;margin:0;padding:0}
html,body{width:1200px;height:2556px;overflow:hidden}
body{background:var(--canvas);font-family:"DM Sans",sans-serif;color:var(--ink);position:relative}
h1,h2,h3,.display{font-family:"Poppins",sans-serif}

/* ---------- main homepage ---------- */
.home{position:absolute;left:0;top:0;width:820px;height:2556px;background:var(--white);overflow:hidden}
.site-header{height:40px;display:flex;align-items:center;justify-content:space-between;padding:0 40px;background:var(--white);border-bottom:1px solid var(--blue-100)}
.brand{display:flex;align-items:center;gap:6px;font-weight:700;font-size:11px;color:var(--blue-900)}
.brand-mark{width:10px;height:10px;border-radius:50%;background:var(--blue-900)}
.nav{display:flex;gap:16px;font-size:8px;color:var(--muted);text-transform:uppercase;letter-spacing:.4px}
.btn{display:inline-block;background:var(--blue-900);color:var(--white);font-weight:700;border-radius:3px;text-transform:uppercase;letter-spacing:.5px}
.site-header .btn{font-size:7px;padding:6px 10px}

.hero{position:relative;height:560px;background:linear-gradient(120deg,#f6fafd 0%,var(--blue-100) 55%,var(--blue-200) 100%)}
.hero-copy{position:absolute;left:40px;top:70px;width:330px}
.eyebrow{font-size:10px;color:var(--blue-700);font-weight:500;margin-bottom:10px}
.hero h1{font-size:34px;line-height:1.12;color:var(--blue-900);font-weight:600}
.hero h1 .thin{color:var(--blue-700);font-weight:500}
.hero p{font-size:10px;line-height:1.6;color:var(--muted);margin-top:16px}
.hero-actions{margin-top:28px;display:flex;align-items:center;gap:14px}
.hero-actions .btn{font-size:8px;padding:10px 16px}
.link{font-size:8px;color:var(--blue-900);font-weight:700;text-transform:uppercase}
.hero-photo{position:absolute;right:0;top:0;width:420px;height:560px;background:linear-gradient(160deg,#dbe8f3 0%,#b9d1e7 45%,#e9e3da 100%)}

.problem{height:360px;padding:40px 80px 0;text-align:center}
.kicker{font-size:9px;color:var(--blue-700);text-transform:uppercase;letter-spacing:.6px}
.problem h2{font-size:24px;line-height:1.25;color:var(--ink);margin-top:8px;font-weight:600}
.problem h2 strong,.focus h2 strong{color:var(--blue-900)}
.problem p{font-size:10px;line-height:1.6;color:var(--muted);margin:14px auto 0;width:560px}
.stats{display:flex;justify-content:space-between;margin-top:40px;padding:0 20px}
.stat{display:flex;align-items:center;gap:10px;text-align:left}
.stat-icon{width:34px;height:34px;border-radius:50%;background:var(--blue-100);display:flex;align-items:center;justify-content:center}
.stat b{display:block;font-family:"Poppins",sans-serif;font-size:22px;color:var(--blue-900);line-height:1}
.stat span{font-size:8px;color:var(--muted)}

.why{position:relative;height:420px;background:linear-gradient(180deg,#fff 0%,var(--blue-100) 100%)}
.why .corner-tl{position:absolute;left:0;top:0}
.why .corner-br{position:absolute;right:0;bottom:0}
.why-title{text-align:center;padding-top:30px}
.why-title h2{font-size:22px;font-weight:600}
.why-title h2 strong{color:var(--blue-900)}
.why-intro{font-size:9px;color:var(--muted);line-height:1.6;width:420px;margin:8px auto 0;text-align:center}
.why-photo{position:absolute;left:70px;top:150px;width:220px;height:220px;border-radius:50%;background:radial-gradient(circle at 45% 40%,#e6d7c8,#9fb9d3 70%);border:6px solid var(--white)}
.why-list{position:absolute;left:340px;top:150px;width:400px}
.why-card{display:flex;gap:12px;background:var(--white);border-radius:6px;padding:12px 14px;margin-bottom:12px;box-shadow:0 4px 14px rgba(0,84,170,.08)}
.why-card .dot{flex:0 0 22px;height:22px;border-radius:50%;background:var(--blue-100);display:flex;align-items:center;justify-content:center}
.why-card h3{font-size:10px;color:var(--ink);font-weight:600}
.why-card p{font-size:8px;color:var(--muted);line-height:1.5;margin-top:3px}
.why-list .btn{font-size:8px;padding:9px 18px;margin-left:120px}

.founder{position:relative;height:500px}
.founder-intro{text-align:center;padding-top:40px}
.founder-intro h2{font-size:26px;color:var(--blue-900);font-weight:600;margin-top:4px}
.founder-intro p{font-size:10px;color:var(--muted);line-height:1.6;width:560px;margin:14px auto 0}
.founder-band{position:absolute;left:0;bottom:0;width:820px;height:220px;background:var(--dark)}
.founder-band p{position:absolute;left:70px;top:70px;width:300px;color:var(--white);font-size:12px;line-height:1.6}
.founder-photo{position:absolute;right:150px;bottom:0;width:220px;height:300px;background:linear-gradient(180deg,#c9d7e6 0%,#3d5d84 100%);border-radius:110px 110px 0 0}

.focus{height:520px;text-align:center;padding-top:50px;background:linear-gradient(180deg,#fff 0%,var(--blue-100) 100%)}
.focus h2{font-size:24px;line-height:1.25;font-weight:600;width:560px;margin:8px auto 0}
.focus p.lead{font-size:10px;color:var(--muted);line-height:1.6;width:560px;margin:14px auto 0}
.focus-cards{display:flex;justify-content:center;gap:22px;margin-top:60px}
.focus-card{width:200px;background:var(--white);border-radius:6px;overflow:hidden;box-shadow:0 6px 18px rgba(0,84,170,.1);text-align:left}
.focus-card .img{height:130px}
.focus-card h3{font-size:10px;padding:10px 12px 2px;color:var(--ink);font-weight:600}
.focus-card p{font-size:8px;color:var(--muted);line-height:1.5;padding:0 12px 12px}
.focus-card.lifted{margin-top:-30px}

.working{height:156px;text-align:center;padding-top:30px}

/* ---------- inner pages column ---------- */
.pages{position:absolute;left:868px;top:0;width:324px;height:2556px}
.pg{position:absolute;left:0;width:324px;overflow:hidden;background:var(--white)}
.mini-title{font-family:"Poppins",sans-serif;font-weight:600;font-size:9px;line-height:1.2;color:var(--ink)}
.mini-title.blue{color:var(--blue-900)}
.mini-title.light{color:var(--white)}
.mini-text{font-size:4px;line-height:1.5;color:var(--muted)}
.bar{height:3px;border-radius:2px;background:var(--blue-200);margin-top:4px}
.mini-btn{display:inline-block;background:var(--blue-900);width:50px;height:10px;border-radius:2px}
.ph{border-radius:4px}
</style>
</head>
<body>

<main class="home">
  <header class="site-header">
    <div class="brand"><span class="brand-mark"></span>The Lanternfield Group</div>
    <nav class="nav"><span>Home</span><span>About</span><span>Services</span><span>Testimonials</span><span>Blog</span><span>Contact</span></nav>
    <span class="btn">Book a Discovery Call</span>
  </header>

  <section class="hero">
    <div class="hero-copy">
      <div class="eyebrow">For Established Wellness And Integrative Clinics</div>
      <h1>Get more <span class="thin">of the right patients</span> without having your whole clinic depend on you.</h1>
      <p>You've built a real practice. People trust you. You also carry the growth, the follow-up and the pressure. We help you see what is holding the business back, fix the right things first, and build a clinic that brings in better-fit patients without everything resting on your shoulders.</p>
      <div class="hero-actions">
        <span class="btn">Book a Growth Audit</span>
        <span class="link">See how it works →</span>
      </div>
    </div>
    <div class="hero-photo" role="img" aria-label="Photo of a practice owner working with a client in a bright studio"></div>
  </section>

  <section class="problem">
    <div class="kicker">You Don't Just Need More Leads</div>
    <h2>The problem is not always more patients. <strong>It is what happens before they book.</strong></h2>
    <p>Most clinic owners do not need more marketing. They need the right people finding them, trusting them, and moving to book. Understanding where each visit falls off is where real, steady growth starts for your practice.</p>
    <div class="stats">
      <div class="stat"><div class="stat-icon"><svg width="16" height="16" viewBox="0 0 16 16"><circle cx="8" cy="8" r="6" fill="none" stroke="#0054AA" stroke-width="1.5"/><path d="M8 4v4l3 2" stroke="#0054AA" stroke-width="1.5" fill="none"/></svg></div><div><b>8+</b><span>Years Experience</span></div></div>
      <div class="stat"><div class="stat-icon"><svg width="16" height="16" viewBox="0 0 16 16"><rect x="2" y="5" width="12" height="9" fill="none" stroke="#0054AA" stroke-width="1.5"/><path d="M6 5V3h4v2" stroke="#0054AA" stroke-width="1.5" fill="none"/></svg></div><div><b>20+</b><span>Businesses Supported</span></div></div>
      <div class="stat"><div class="stat-icon"><svg width="16" height="16" viewBox="0 0 16 16"><rect x="2" y="3" width="12" height="8" fill="none" stroke="#0054AA" stroke-width="1.5"/><path d="M5 14h6" stroke="#0054AA" stroke-width="1.5"/></svg></div><div><b>50+</b><span>Digital Assets Reviewed</span></div></div>
      <div class="stat"><div class="stat-icon"><svg width="16" height="16" viewBox="0 0 16 16"><path d="M2 13l4-4 3 3 5-6" stroke="#0054AA" stroke-width="1.5" fill="none"/></svg></div><div><b>15+</b><span>Growth Projects Completed</span></div></div>
    </div>
  </section>

  <section class="why">
    <svg class="corner-tl" width="70" height="90" viewBox="0 0 70 90"><path d="M0 0h70L0 90z" fill="#7BADD7"/></svg>
    <svg class="corner-br" width="90" height="120" viewBox="0 0 90 120"><path d="M90 0v120H0z" fill="#0677BA"/></svg>
    <div class="why-title">
      <div class="kicker">If None Of This Sounds Familiar, You're In The Right Place</div>
      <h2>Why <strong>Growing Your Wellness</strong> Practice still feels harder than it should.</h2>
      <p class="why-intro">It can be more than a busy schedule. Often the problem is that the parts that bring patients in do not work together, so the whole load keeps landing back on you.</p>
    </div>
    <div class="why-photo" role="img" aria-label="Portrait photo of a thoughtful practice owner"></div>
    <div class="why-list">
      <div class="why-card"><div class="dot"><svg width="10" height="10"><path d="M2 5l2 2 4-4" stroke="#0054AA" stroke-width="1.5" fill="none"/></svg></div><div><h3>You Work Hard Depends on You</h3><p>The clinic runs well when you are there, but growth stalls as soon as you step back from the daily work.</p></div></div>
      <div class="why-card"><div class="dot"><svg width="10" height="10"><path d="M2 5l2 2 4-4" stroke="#0054AA" stroke-width="1.5" fill="none"/></svg></div><div><h3>You're Getting Inquiries, But Not Enough…</h3><p>People call and click, yet too few become booked, returning patients who fit the work you love.</p></div></div>
      <div class="why-card"><div class="dot"><svg width="10" height="10"><path d="M2 5l2 2 4-4" stroke="#0054AA" stroke-width="1.5" fill="none"/></svg></div><div><h3>Referrals Are Doing The Most Of You…</h3><p>Word of mouth is great, but it should not be the only thing keeping your schedule full each month.</p></div></div>
      <span class="btn">Learn More</span>
    </div>
  </section>

  <section class="founder">
    <div class="founder-intro">
      <div class="kicker">Meet The Founder</div>
      <h2>Hi, I'm Elias.</h2>
      <p>I help wellness clinic owners figure out why growth still feels harder than it should and where to fix it first. The goal is not to hand you more things to manage. The goal is to help you make better decisions, support the team, and build a practice that feels calmer, clearer and more profitable.</p>
    </div>
    <div class="founder-band">
      <p>You do not need more noise. You need the right pieces working together so your clinic feels trusted before someone ever picks up the phone.</p>
      <div class="founder-photo" role="img" aria-label="Photo of the founder in a suit"></div>
    </div>
  </section>

  <section class="focus">
    <div class="kicker">How We Help Wellness Clients</div>
    <h2>This is not about chasing more leads. <strong>It is about building a clinic that works better.</strong></h2>
    <p class="lead">Most clinic owners do not struggle from lack of effort. They are busy, skilled and trusted. The real issue is that the parts of growth are not joined up. We bring clarity, structure and focus so the right patients find you, trust you and book.</p>
    <div class="focus-cards">
      <div class="focus-card"><div class="img" style="background:linear-gradient(135deg,#cfe0ef,#8fb3d6)" role="img" aria-label="Photo of a strategy meeting"></div><h3>Know Where To Focus</h3><p>See what matters most and fix that first.</p></div>
      <div class="focus-card lifted"><div class="img" style="background:linear-gradient(135deg,#e8e1d6,#a9c3dd)" role="img" aria-label="Photo of a practice owner greeting a client"></div><h3>Build Trust Before the First Call</h3><p>Let your website and messaging answer doubts and bring in people who fit.</p></div>
      <div class="focus-card"><div class="img" style="background:linear-gradient(135deg,#d6e4f0,#7ea6cf)" role="img" aria-label="Photo of a clinic team working together"></div><h3>Take Pressure Off the Team</h3><p>Clear systems so growth does not rest on you.</p></div>
    </div>
  </section>

  <section class="working"><div class="kicker">What's Working</div></section>
</main>

<aside class="pages" aria-label="Inner page layouts">
  <div class="pg" style="top:0;height:200px;background:linear-gradient(120deg,#f6fafd,var(--blue-100))">
    <div style="padding:6px 10px;display:flex;justify-content:space-between;align-items:center"><span style="font-size:5px;font-weight:700;color:var(--blue-900)">The Lanternfield Group</span><span class="mini-btn" style="width:34px;height:7px"></span></div>
    <div style="position:absolute;left:12px;top:40px;width:150px"><div class="mini-title blue" style="font-size:12px">Get more of the right patients</div><div class="mini-text" style="margin-top:6px">without having your whole clinic depend on you.</div><div class="bar" style="width:120px"></div><div class="bar" style="width:100px"></div><div class="mini-btn" style="margin-top:10px"></div></div>
    <div class="ph" style="position:absolute;right:0;top:20px;width:140px;height:180px;background:linear-gradient(160deg,#dbe8f3,#b9d1e7)" role="img" aria-label="Hero photo of two people working together"></div>
  </div>
  <div class="pg" style="top:206px;height:110px;padding:12px;text-align:center">
    <div class="mini-title">The problem is not always more patients.</div>
    <div class="bar" style="width:200px;margin:6px auto 0"></div><div class="bar" style="width:160px;margin:4px auto 0"></div>
    <div style="display:flex;justify-content:space-around;margin-top:16px"><b style="color:var(--blue-900);font-size:10px">8+</b><b style="color:var(--blue-900);font-size:10px">20+</b><b style="color:var(--blue-900);font-size:10px">50+</b><b style="color:var(--blue-900);font-size:10px">15+</b></div>
  </div>
  <div class="pg" style="top:322px;height:140px;background:var(--blue-100)">
    <div class="mini-title" style="text-align:center;padding-top:10px">Why growing still feels harder</div>
    <div style="position:absolute;left:20px;top:36px;width:90px;height:90px;border-radius:50%;background:radial-gradient(circle,#e6d7c8,#9fb9d3)" role="img" aria-label="Portrait photo"></div>
    <div style="position:absolute;left:130px;top:36px;width:170px"><div style="height:22px;background:#fff;border-radius:3px;margin-bottom:6px"></div><div style="height:22px;background:#fff;border-radius:3px;margin-bottom:6px"></div><div style="height:22px;background:#fff;border-radius:3px"></div></div>
  </div>
  <div class="pg" style="top:468px;height:150px">
    <div class="mini-title blue" style="text-align:center;padding-top:14px">Hi, I'm Elias.</div>
    <div class="bar" style="width:220px;margin:6px auto 0"></div><div class="bar" style="width:180px;margin:4px auto 0"></div>
    <div style="position:absolute;left:0;bottom:0;width:324px;height:80px;background:var(--dark)"><div class="bar" style="position:absolute;left:20px;top:30px;width:100px;background:#555"></div><div style="position:absolute;right:50px;bottom:0;width:70px;height:95px;border-radius:35px 35px 0 0;background:linear-gradient(#c9d7e6,#3d5d84)" role="img" aria-label="Founder photo"></div></div>
  </div>
  <div class="pg" style="top:624px;height:130px;background:linear-gradient(#fff,var(--blue-100))">
    <div class="mini-title" style="text-align:center;padding-top:10px">It is about building a clinic that works.</div>
    <div style="display:flex;gap:8px;justify-content:center;margin-top:14px"><div style="width:86px;height:80px;background:linear-gradient(#cfe0ef,#fff 60%);border-radius:3px"></div><div style="width:86px;height:80px;background:linear-gradient(#e8e1d6,#fff 60%);border-radius:3px"></div><div style="width:86px;height:80px;background:linear-gradient(#d6e4f0,#fff 60%);border-radius:3px"></div></div>
  </div>
  <div class="pg" style="top:760px;height:170px;padding:12px">
    <div class="mini-title">Work with a strategist who knows wellness</div>
    <div class="bar" style="width:240px"></div>
    <div style="display:flex;gap:8px;margin-top:14px"><div class="ph" style="flex:1;height:90px;background:linear-gradient(#b9d1e7,#7BADD7)" role="img" aria-label="Team photo"></div><div class="ph" style="flex:1;height:90px;background:linear-gradient(#e6d7c8,#b9d1e7)" role="img" aria-label="Client meeting photo"></div><div class="ph" style="flex:1;height:90px;background:linear-gradient(#cfe0ef,#0677BA)" role="img" aria-label="Workshop photo"></div></div>
  </div>
  <div class="pg" style="top:936px;height:90px;background:var(--blue-100);padding:14px;text-align:center">
    <div class="mini-title blue">Clarity first, then growth</div><div class="bar" style="width:200px;margin:6px auto 0"></div><div class="mini-btn" style="margin-top:12px"></div>
  </div>
  <div class="pg" style="top:1032px;height:150px;background:var(--navy)">
    <div style="position:absolute;left:16px;top:40px;width:140px"><div class="mini-title light">Lead a practice that grows without you</div><div class="bar" style="background:#3b5a80;width:120px"></div><div class="bar" style="background:#3b5a80;width:90px"></div></div>
    <div style="position:absolute;right:30px;bottom:0;width:100px;height:130px;border-radius:50px 50px 0 0;background:linear-gradient(#c9d7e6,#3d5d84)" role="img" aria-label="Photo of the founder"></div>
  </div>
  <div class="pg" style="top:1188px;height:120px;padding:14px;text-align:center">
    <div class="mini-title">What clinic owners say</div>
    <div style="margin:10px auto 0;width:260px;height:60px;background:var(--blue-100);border-radius:4px"></div>
  </div>
  <div class="pg" style="top:1314px;height:140px;padding:14px">
    <div class="mini-title" style="text-align:center">How we help</div>
    <div style="display:grid;grid-template-columns:repeat(4,1fr);gap:8px;margin-top:14px">
      <div style="height:70px;background:var(--blue-100);border-radius:3px"></div><div style="height:70px;background:var(--blue-100);border-radius:3px"></div><div style="height:70px;background:var(--blue-100);border-radius:3px"></div><div style="height:70px;background:var(--blue-100);border-radius:3px"></div>
    </div>
  </div>
  <div class="pg" style="top:1460px;height:150px;background:linear-gradient(#fff,var(--blue-100))">
    <div style="position:absolute;left:16px;top:30px;width:130px"><div class="mini-title">See the holes in the bucket</div><div class="bar" style="width:110px"></div><div class="bar" style="width:90px"></div><div class="mini-btn" style="margin-top:10px"></div></div>
    <div class="ph" style="position:absolute;right:16px;top:26px;width:150px;height:100px;background:linear-gradient(135deg,#cfe0ef,#7BADD7)" role="img" aria-label="Photo of a laptop showing a clinic website"></div>
  </div>
  <div class="pg" style="top:1616px;height:290px;padding:14px">
    <div class="mini-title" style="text-align:center">Our approach</div>
    <div style="display:grid;grid-template-columns:1fr 1fr;gap:10px;margin-top:14px">
      <div style="height:110px;border:1px solid var(--blue-200);border-radius:4px"></div><div style="height:110px;border:1px solid var(--blue-200);border-radius:4px"></div>
      <div style="height:110px;border:1px solid var(--blue-200);border-radius:4px"></div><div style="height:110px;border:1px solid var(--blue-200);border-radius:4px"></div>
    </div>
  </div>
  <div class="pg" style="top:1912px;height:190px;background:var(--blue-100);padding:14px">
    <div class="mini-title blue" style="text-align:center">Results from real practices</div>
    <div style="display:flex;gap:8px;margin-top:14px"><div class="ph" style="flex:1;height:120px;background:linear-gradient(#e6d7c8,#9fb9d3)" role="img" aria-label="Client photo"></div><div class="ph" style="flex:1;height:120px;background:linear-gradient(#cfe0ef,#7BADD7)" role="img" aria-label="Client photo"></div><div class="ph" style="flex:1;height:120px;background:linear-gradient(#d6e4f0,#0677BA)" role="img" aria-label="Client photo"></div></div>
  </div>
  <div class="pg" style="top:2108px;height:190px;padding:14px">
    <div class="mini-title" style="text-align:center">Frequently asked questions</div>
    <div style="margin-top:14px"><div style="height:20px;border-bottom:1px solid var(--blue-200)"></div><div style="height:20px;border-bottom:1px solid var(--blue-200)"></div><div style="height:20px;border-bottom:1px solid var(--blue-200)"></div><div style="height:20px;border-bottom:1px solid var(--blue-200)"></div><div style="height:20px;border-bottom:1px solid var(--blue-200)"></div></div>
  </div>
  <div class="pg" style="top:2304px;height:252px;background:var(--navy);padding:30px 14px;text-align:center">
    <div class="mini-title light">Ready to see what is holding your clinic back?</div>
    <div class="mini-btn" style="margin-top:14px;background:var(--white)"></div>
    <div style="border-top:1px solid #2a4467;margin-top:60px;padding-top:14px;font-size:5px;color:var(--blue-400);font-weight:700">The Lanternfield Group</div>
  </div>
</aside>

</body>
</html>
```